TR Advisory Business Cards - High End AV / Low Voltage Company

We are low voltage AV company that specializes in high end clients on the residential side and larger businesses on the commercial side. We want something modern, tech looking but also something that is extremely professional looking. We have uploaded our logos and postcards we already have in the field. Along with a picture of one of our wrapped vans. Our website is at www.trvadvisory.example and our primary colors are the orange, green, grey and blue all military color finishes.

We are interesting in the slogans "Pairing You with the Right Technology" or "Connecting the Coast with Tech"

Target Market(s)

We focus on 70% Commercial and 30% Residential Customers

Industry/Entity Type

Low Voltage, AV Company

Contact Information for Business Card

Name - Dorian Fairweather, Title - Owner, Office Phone - 555-714-3096, Mobile Phone - 555-802-4173, E-Mail - d@trvadvisory.example, Website: www.trvadvisory.example

Font styles to use
Sans Serif

Requirements
Must have
• Must have Name, Title, Work Phone & Mobile, Website and Logo.
Nice to have
• We want something that will impress our higher end clients with a great logo
Should not have
• Too traditional or plain.

```html
<!DOCTYPE html>
<html lang="en">
<head>
<meta charset="utf-8">
<title>TR Advisory Business Cards</title>
<link rel="stylesheet" href="https://fonts.googleapis.com/css2?family=Montserrat:wght@600;700&family=Questrial&display=swap">
<style>
  :root {
    --backdrop: #c8c8c8;
    --orange: #f0703d;
    --orange-deep: #ea6533;
    --orange-light: #f67d49;
    --white: #ffffff;
    --ink: #1f1f1f;
    --band: #f1f1f1;
  }
  * { box-sizing: border-box; margin: 0; padding: 0; }
  html, body {
    width: 1200px; height: 900px; overflow: hidden;
    background: var(--backdrop);
  }
  .canvas { position: relative; width: 1200px; height: 900px; }

  .card {
    position: absolute;
    width: 560px; height: 320px;
    border-radius: 26px;
    overflow: hidden;
  }

  /* Front */
  .card-front {
    left: 90px; top: 100px;
    background: linear-gradient(135deg, var(--orange-light), var(--orange-deep));
    display: flex; flex-direction: column; align-items: center; justify-content: center;
    gap: 26px;
  }
  .front-brand { display: flex; align-items: center; gap: 18px; }
  .brand-dot {
    flex: none;
    width: 54px; height: 54px; border-radius: 50%;
    border: 5px solid var(--white);
  }
  .front-brand .brand-name {
    font-family: "Montserrat", sans-serif; font-weight: 700;
    font-size: 44px; letter-spacing: 3px; color: var(--white);
    text-transform: uppercase; white-space: nowrap;
  }
  .slogan {
    font-family: "Montserrat", sans-serif; font-weight: 600;
    font-size: 13px; letter-spacing: 2px; color: var(--white);
    text-transform: uppercase; white-space: nowrap;
  }

  /* Back */
  .card-back {
    left: 550px; top: 480px;
    background: var(--white);
  }
  .back-band {
    position: absolute; right: 0; top: 0; width: 210px; height: 100%;
    background: var(--band);
  }
  .back-brand {
    position: absolute; left: 40px; top: 46px;
    display: flex; align-items: center; gap: 12px;
  }
  .back-brand .brand-dot { width: 36px; height: 36px; border: 4px solid var(--orange); }
  .back-brand .brand-name {
    font-family: "Montserrat", sans-serif; font-weight: 700;
    font-size: 26px; letter-spacing: 2px; color: var(--orange);
    text-transform: uppercase; white-space: nowrap;
  }
  .person { position: absolute; left: 40px; top: 160px; }
  .person-name {
    font-family: "Montserrat", sans-serif; font-weight: 700;
    font-size: 19px; letter-spacing: 1px; color: var(--orange);
    text-transform: uppercase; white-space: nowrap;
  }
  .person-title {
    font-family: "Questrial", sans-serif; font-size: 18px; color: var(--ink);
    margin-top: 2px;
  }
  .contact-list { list-style: none; margin-top: 14px; }
  .contact-list li, .web-list li {
    display: flex; align-items: center; gap: 8px;
    font-family: "Questrial", sans-serif; font-size: 17px; color: var(--ink);
    line-height: 24px; white-space: nowrap;
  }
  .icon { width: 18px; height: 18px; flex: none; }
  .web-list {
    list-style: none;
    position: absolute; right: 22px; bottom: 40px;
    text-align: right;
  }
  .web-list li { justify-content: flex-end; }
  .accent { color: var(--orange); }
</style>
</head>
<body>
<main class="canvas">

  <section class="card card-front" aria-label="Card front">
    <div class="front-brand">
      <span class="brand-dot"></span>
      <span class="brand-name">TR Advisory</span>
    </div>
    <p class="slogan">Connecting the Coast with Tech</p>
  </section>

  <section class="card card-back" aria-label="Card back">
    <div class="back-band"></div>

    <div class="back-brand">
      <span class="brand-dot"></span>
      <span class="brand-name">TR Advisory</span>
    </div>

    <div class="person">
      <p class="person-name">Dorian Fairweather</p>
      <p class="person-title">Owner</p>
      <ul class="contact-list">
        <li>
          <svg class="icon" viewBox="0 0 20 20" aria-hidden="true"><circle cx="10" cy="10" r="9" fill="none" stroke="#f0703d" stroke-width="1.6"/><path d="M7 5.5l1.6 2-1 1.2a6 6 0 0 0 3.7 3.7l1.2-1 2 1.6-1 1.5c-3.8-.3-7.3-3.8-7.6-7.6z" fill="#f0703d"/></svg>
          555-714-3096
        </li>
        <li>
          <svg class="icon" viewBox="0 0 20 20" aria-hidden="true"><circle cx="10" cy="10" r="9" fill="none" stroke="#f0703d" stroke-width="1.6"/><rect x="7" y="5" width="6" height="10" rx="1" fill="none" stroke="#f0703d" stroke-width="1.4"/><circle cx="10" cy="13" r=".8" fill="#f0703d"/></svg>
          555-802-4173
        </li>
      </ul>
    </div>

    <ul class="web-list">
      <li>
        d@trvadvisory.example
        <svg class="icon" viewBox="0 0 20 20" aria-hidden="true"><circle cx="10" cy="10" r="9" fill="none" stroke="#f0703d" stroke-width="1.6"/><rect x="5.5" y="6.5" width="9" height="7" fill="none" stroke="#f0703d" stroke-width="1.3"/><path d="M5.5 6.5l4.5 4 4.5-4" fill="none" stroke="#f0703d" stroke-width="1.3"/></svg>
      </li>
      <li>
        <span>www.<span class="accent">trvadvisory</span>.example</span>
        <svg class="icon" viewBox="0 0 20 20" aria-hidden="true"><circle cx="10" cy="10" r="9" fill="none" stroke="#f0703d" stroke-width="1.6"/><circle cx="10" cy="10" r="5" fill="none" stroke="#f0703d" stroke-width="1.2"/><ellipse cx="10" cy="10" rx="2" ry="5" fill="none" stroke="#f0703d" stroke-width="1.1"/><path d="M5 10h10" stroke="#f0703d" stroke-width="1.1"/></svg>
      </li>
    </ul>
  </section>

</main>
</body>
</html>
```